Business Card Design

Lawyer
Business name "HallorenLaw"
Areas of expertise:
property
commercial
trusts
immigration
franchising
I want the following quote on the back of the card somewhere.
"Education is when you read the fine print,
experience is what you get if you don't." Clem Varnody
Probably the "areas of expertise" should be on the back also to avoid cluttering the front.
As for colours, I like the shades of blue used on qelvobank.com.
The basic part of the card with the contact info needs to be white and uncluttered.
Target Market(s)
small to medium sized self employed business people
Industry/Entity Type
Business
Contact Information for Business Card
Dwight Halloren
Phone + 64 9 415 3067
Fax: + 64 9 415 3066
PO Box 742
Clevedon
Auckland 2248
NZ
email: dwight@ferncastlaw.example.co.nz

```html
<!DOCTYPE html>
<html lang="en">
<head>
<meta charset="utf-8">
<title>HallorenLaw – Business Card</title>
<link rel="stylesheet" href="https://fonts.googleapis.com/css2?family=Fira+Sans:wght@300&display=swap">
<style>
  :root {
    --navy-centre: #043f6e;
    --navy-mid: #02345f;
    --navy-edge: #012352;
    --rule-blue: #4b9dd3;
    --title-blue: #6cc2ef;
    --name-white: #ffffff;
  }
  html, body {
    margin: 0;
    padding: 0;
    width: 1200px;
    height: 740px;
    overflow: hidden;
  }
  .card {
    position: relative;
    width: 1200px;
    height: 740px;
    background: radial-gradient(ellipse 62% 62% at 50% 45%, var(--navy-centre) 0%, var(--navy-mid) 55%, var(--navy-edge) 100%);
    font-family: "Fira Sans", "Segoe UI", sans-serif;
    font-weight: 300;
  }
  .card__name {
    position: absolute;
    left: 0;
    right: 0;
    top: 308px;
    margin: 0;
    text-align: center;
    color: var(--name-white);
    font-size: 76px;
    font-weight: 300;
    line-height: 90px;
    letter-spacing: 0.5px;
  }
  .card__rule {
    position: absolute;
    left: 0;
    top: 397px;
    width: 1200px;
    height: 3px;
    background: var(--rule-blue);
  }
  .card__role {
    position: absolute;
    left: 0;
    right: 0;
    top: 403px;
    margin: 0;
    text-align: center;
    color: var(--title-blue);
    font-size: 46px;
    line-height: 56px;
    letter-spacing: 0.5px;
  }
</style>
</head>
<body>
  <main class="card">
    <h1 class="card__name">Halloren Law</h1>
    <div class="card__rule"></div>
    <p class="card__role">Lawyer</p>
  </main>
</body>
</html>
```